Info Graphic for our IT Staff Augmentation Page

Our offering would be:
-Programmers
-Project Managers
-Testers
-Solutions Architects
-Designers
-Applications Adminstrators
-Network Administrators
-PC/Help Desk Support

We would offer: Onsite | Offsite | Remote

Please see our Website for Content Ideas:
http://staging.velrowtechgroup.com/staff-augmentation/

**** The background video will not stay there in the header. We would be looking to replace with your info graphic. Dimensions should be at least 2000 x 400

Industry/Entity Type

It Support

Requirements
Should not have
• The example info graphic uploaded here is to show the scope of the project. Do not try to simply duplicate...will be rejected and you will waist your time and mine. Please create an interpretation with the service offerings included and look at the existing content in the staff augmentation page to get ideas.

```html
<!DOCTYPE html>
<html lang="en">
<head>
<meta charset="utf-8">
<title>Velrow Tech Group – IT Staff Augmentation</title>
<link rel="stylesheet" href="https://fonts.googleapis.com/css2?family=Cabin:wght@400;500&family=Raleway:wght@700&family=Kalam:wght@400;700&display=swap">
<style>
  :root {
    --bg-dark: #2b2a2c;
    --bg-mid: #4a4949;
    --bg-light: #8a8886;
    --header-bg: rgba(30, 30, 34, 0.72);
    --rule: rgba(255, 255, 255, 0.55);
    --accent: #ffe81c;
    --accent-deep: #e8cc00;
    --text-light: #ffffff;
    --text-dark: #2a2a2a;
  }
  * { margin: 0; padding: 0; box-sizing: border-box; }
  html, body { width: 1200px; height: 460px; overflow: hidden; background: var(--bg-dark); }

  .banner {
    position: relative;
    width: 1200px;
    height: 460px;
    overflow: hidden;
    background:
      radial-gradient(ellipse 620px 260px at 720px 250px, rgba(170,168,165,0.55), transparent 70%),
      linear-gradient(100deg, var(--bg-dark) 0%, var(--bg-mid) 35%, #6d6b69 60%, var(--bg-mid) 85%, #3a3939 100%);
  }
  .backdrop { position: absolute; inset: 0; }

  .site-header {
    position: absolute;
    top: 0; left: 0;
    width: 1200px;
    height: 92px;
    background: var(--header-bg);
    border-top: 1px solid #4d6fb3;
    border-bottom: 1px solid var(--rule);
  }
  .brand {
    position: absolute;
    left: 116px;
    top: 30px;
    display: flex;
    align-items: center;
    gap: 10px;
    font-family: "Cabin", sans-serif;
    font-weight: 500;
    font-size: 26px;
    color: var(--text-light);
    letter-spacing: 0.3px;
  }
  .brand-mark { width: 28px; height: 28px; background: var(--accent); }

  .main-nav {
    position: absolute;
    top: 38px;
    left: 742px;
    display: flex;
    align-items: center;
    gap: 31px;
    font-family: "Raleway", sans-serif;
    font-weight: 700;
    font-size: 14px;
    color: var(--text-light);
    letter-spacing: 0.2px;
  }
  .search-icon { width: 13px; height: 13px; margin-left: -2px; }

  .offer-title {
    position: absolute;
    left: 182px;
    top: 118px;
    width: 300px;
    text-align: center;
    font-family: "Kalam", cursive;
  }
  .offer-lead { font-size: 28px; font-weight: 700; color: var(--accent-deep); line-height: 34px; }
  .offer-modes { font-size: 27px; color: var(--text-light); line-height: 34px; }
  .offer-modes .sep { display: inline-block; width: 2px; height: 34px; background: var(--text-light); vertical-align: middle; margin: 0 12px; }

  .globe-art { position: absolute; left: 195px; top: 185px; }

  .join-bubble { position: absolute; left: 570px; top: 272px; }
  .join-label {
    position: absolute;
    left: 577px;
    top: 318px;
    width: 122px;
    text-align: center;
    font-family: "Kalam", cursive;
    font-size: 30px;
    color: var(--text-dark);
  }

  .role-list {
    position: absolute;
    left: 784px;
    top: 148px;
    list-style: none;
    font-family: "Cabin", sans-serif;
    font-size: 19.5px;
    color: var(--text-light);
  }
  .role-list li { display: flex; align-items: center; height: 30.3px; }
  .role-list li::before {
    content: "";
    width: 14px; height: 14px;
    border-radius: 50%;
    background: var(--accent);
    margin-right: 16px;
    flex: none;
  }
</style>
</head>
<body>
<main class="banner">
  <svg class="backdrop" width="1200" height="460" role="img" aria-label="Blurred photo of an office with light beams">
    <defs>
      <linearGradient id="beam" x1="0" y1="0" x2="1" y2="0">
        <stop offset="0" stop-color="#ffffff" stop-opacity="0"/>
        <stop offset="0.6" stop-color="#ffffff" stop-opacity="0.12"/>
        <stop offset="1" stop-color="#ffffff" stop-opacity="0"/>
      </linearGradient>
    </defs>
    <polygon points="380,300 1200,120 1200,220" fill="url(#beam)"/>
    <polygon points="380,300 1200,330 1200,420" fill="url(#beam)"/>
  </svg>

  <header class="site-header">
    <div class="brand"><span class="brand-mark"></span>Velrow Tech Group</div>
    <nav class="main-nav">
      <span>SERVICES</span>
      <span>PROJECTS</span>
      <span>BLOG</span>
      <span>CONTACT</span>
      <svg class="search-icon" viewBox="0 0 14 14" aria-label="Search">
        <circle cx="5.8" cy="5.8" r="4.3" fill="none" stroke="#fff" stroke-width="2.2"/>
        <line x1="9" y1="9" x2="13" y2="13" stroke="#fff" stroke-width="2.6" stroke-linecap="round"/>
      </svg>
    </nav>
  </header>

  <div class="offer-title">
    <div class="offer-lead">We would offer</div>
    <div class="offer-modes">Onsite<span class="sep"></span>Offsite<span class="sep"></span>Remote</div>
  </div>

  <svg class="globe-art" width="360" height="275" role="img" aria-label="Illustration of a yellow globe circled by a cursor arrow trail">
    <defs>
      <radialGradient id="globe-fill" cx="0.45" cy="0.4" r="0.65">
        <stop offset="0" stop-color="#fff26a"/>
        <stop offset="0.7" stop-color="#e9d000"/>
        <stop offset="1" stop-color="#b9a400"/>
      </radialGradient>
      <radialGradient id="globe-glow" cx="0.5" cy="0.5" r="0.5">
        <stop offset="0" stop-color="#fff9b0" stop-opacity="0.8"/>
        <stop offset="1" stop-color="#fff9b0" stop-opacity="0"/>
      </radialGradient>
    </defs>
    <ellipse cx="128" cy="218" rx="90" ry="30" fill="url(#globe-glow)"/>
    <circle cx="128" cy="113" r="106" fill="url(#globe-fill)"/>
  </svg>

  <svg class="join-bubble" width="170" height="130" aria-hidden="true">
    <path d="M68 6 a61 61 0 1 0 52 93 L163 113 L124 84 A61 61 0 0 0 68 6 Z" fill="var(--accent)"/>
  </svg>
  <div class="join-label">Join Us</div>

  <ul class="role-list">
    <li>Programmers</li>
    <li>Project Managers</li>
    <li>Testers</li>
    <li>Solutions Architects</li>
    <li>Designers</li>
    <li>Applications Adminstrators</li>
    <li>Network Administrators</li>
    <li>PC/Help Desk Support</li>
  </ul>
</main>
</body>
</html>
```